Quorvia.app is a developing company for entrepreneurs who need legal services.

Our Company Slogan is : Legal Made Simple
Company Info:
Quorvia is built to help anyone sort through the confusion of taking an idea from thoughts to a tangible reality, legally. We are here to help make the incorporation, idea protection and any other legal necessities an after thought for you. If you know your idea is the next Zentrix we will help you make the right legal decisions from the start.
Subscription Model packages: 2.99, 4.99, 9.99 options in three separate boxes. Choose a monthly option and get started with your startups legal services. Start Now!
Follow us on Social: @quorvia.app
Website template look:
Build an app landing page for the company. Need a clean subscription based template with my updated logo and color scheme to create a landing page, team, and contact page. I want to be able to edit the copy. Very simple and clean using company colors.
Target Market(s)
Gen-Z or Millenial aged entrepreneurs starting a business for the first time.
Industry/Entity Type
Legal
Coding
Coded - Design and coding required
Number of Pages Required
3 page
Font styles to use
Other font styles liked:
- Roboto, or Museo Sans 300,700
Look and feel

```html
<!DOCTYPE html>
<html lang="en">
<head>
<meta charset="utf-8">
<title>Quorvia.app — Legal Made Simple</title>
<link href="https://fonts.googleapis.com/css2?family=Fira+Sans:wght@300;400;500;600&display=swap" rel="stylesheet">
<style>
:root{
  --blue:#38b6f5;
  --blue-text:#3cb4ea;
  --green:#9ccf50;
  --grad-start:#8fca5c;
  --grad-end:#38b7f8;
  --ink:#2f2f2f;
  --muted:#666;
  --soft-bg:#f7f7f5;
  --band-bg:#f5f5f5;
  --line:#e6e6e6;
  --white:#fff;
}
*{margin:0;padding:0;box-sizing:border-box}
html,body{width:769px;height:1200px;overflow:hidden}
body{position:relative;background:var(--white);font-family:"Fira Sans",Arial,sans-serif;color:var(--ink)}
.abs{position:absolute}

/* header */
.site-header{left:0;top:0;width:769px;height:68px}
.brand{left:97px;top:22px;display:flex;align-items:center;gap:6px}
.brand-dot{width:18px;height:18px;border-radius:50%;background:var(--blue)}
.brand-name{font-size:16px;font-weight:500;color:var(--blue);line-height:1}
.brand-tag{font-size:6px;letter-spacing:1px;color:var(--muted);margin-top:2px}
.main-nav{top:28px;left:515px;font-size:10px}
.main-nav a{position:absolute;white-space:nowrap;color:var(--ink);text-decoration:none}
.main-nav a.is-active{color:var(--blue-text)}

/* hero */
.hero{left:0;top:68px;width:769px;height:364px;background:var(--soft-bg)}
.hero-title{left:97px;top:170px;font-size:22px;font-weight:300;color:var(--blue-text);line-height:26px}
.hero-copy{left:97px;top:238px;font-size:9.5px;color:var(--muted);line-height:12px;font-weight:300}
.hero-rule{left:97px;top:279px;width:205px;height:1px;background:#bdbdbd}
.btn-gradient{left:97px;top:300px;width:96px;height:26px;border-radius:2px;background:linear-gradient(90deg,var(--grad-start),var(--grad-end));color:var(--white);font-size:10px;font-weight:600;display:flex;align-items:center;justify-content:center}
.hero-device{left:476px;top:100px;width:148px;height:300px;border-radius:22px;background:#1d1d1d;padding:6px}
.hero-device .screen{width:100%;height:100%;border-radius:17px;background:linear-gradient(180deg,var(--grad-start),var(--grad-end))}

/* section headings */
.section-title{left:0;width:769px;text-align:center;font-weight:300;color:var(--blue-text);font-size:21px}
.title-rule{height:1px;background:#c7dd9e}

/* about */
.about-copy{left:60px;top:510px;width:649px;text-align:center;font-size:9.5px;line-height:15.6px;color:var(--ink)}

/* packages */
.packages{left:0;top:595px;width:769px;height:343px;background:var(--band-bg)}
.package-card{top:687px;width:175px;height:203px;background:var(--white);border:1px solid #ececec;border-radius:2px}
.package-head{position:absolute;left:8px;top:9px;width:160px;height:38px;background:linear-gradient(90deg,var(--grad-start),var(--grad-end));color:var(--white);font-size:13px;display:flex;align-items:center;justify-content:center}
.feature-list{position:absolute;left:37px;top:64px;width:100px;list-style:none}
.feature-list li{height:28px;display:flex;align-items:center;gap:9px;font-size:10px;border-bottom:1px solid var(--line)}
.feature-list li:last-child{border-bottom:none}
.feature-list svg{flex:none}
.btn-start{position:absolute;left:49px;top:162px;width:77px;height:21px;background:var(--green);color:var(--white);font-size:9px;font-weight:300;display:flex;align-items:center;justify-content:center;border-radius:1px}

/* gallery */
.gallery-tile{top:963px;width:187px;height:162px}

/* footer */
.site-footer{left:0;top:1149px;width:769px;height:51px;background:var(--blue)}
.footer-nav{left:95px;top:1168px;font-size:9.5px;color:var(--white);white-space:nowrap}
.footer-nav span{margin:0 5px}
.footer-brand{left:471px;top:1165px;display:flex;align-items:center;gap:5px;color:var(--white)}
.footer-brand .brand-dot{background:var(--white)}
.footer-brand .brand-name{color:var(--white);font-size:14px}
.footer-brand .brand-tag{color:var(--white)}
.social{left:581px;top:1165px;display:flex;gap:5px}
.social span{width:19px;height:19px;border-radius:50%;background:#a9dcf6}
</style>
</head>
<body>

<header class="site-header abs">
  <div class="brand abs">
    <span class="brand-dot"></span>
    <div><div class="brand-name">Quorvia</div><div class="brand-tag">Legal Made Simple</div></div>
  </div>
  <nav class="main-nav abs">
    <a href="#" style="left:0">Home</a>
    <a href="#" class="is-active" style="left:45px">Our Team</a>
    <a href="#" style="left:109px">Contact Us</a>
  </nav>
</header>

<section class="hero abs"></section>
<h1 class="hero-title abs">Start your subscription<br>through Quorvia.app</h1>
<p class="hero-copy abs">Lorem ipsum dolor sit amet, consectetur adipiscing<br>ornare dolor, sed venenatis leo. Integer</p>
<div class="hero-rule abs"></div>
<a class="btn-gradient abs">Get Started</a>
<div class="hero-device abs" role="img" aria-label="Phone showing the Quorvia app splash screen"><div class="screen"></div></div>

<h2 class="section-title abs" style="top:468px">About us</h2>
<div class="title-rule abs" style="left:318px;top:498px;width:133px"></div>
<p class="about-copy abs">Quorvia is built to help anyone sort through the confusion of taking an idea from thoughts to a tangible reality, legally.<br>We are here to help make the incorporation, idea protection and any other legal necessities an after thought<br>for you. If you know your idea is the next Zentrix we will help you make the right legal decisions from the start.</p>

<section class="packages abs"></section>
<h2 class="section-title abs" style="top:636px">Subscription Model Packages</h2>
<div class="title-rule abs" style="left:318px;top:666px;width:133px"></div>

<div class="package-card abs" style="left:95px">
  <div class="package-head">Packages: 2.99</div>
  <ul class="feature-list">
    <li><svg width="11" height="11" viewBox="0 0 11 11"><circle cx="5.5" cy="5.5" r="5" fill="none" stroke="#38b6f5"/><path d="M3 5.6l1.7 1.7L8 4" fill="none" stroke="#38b6f5" stroke-width="1.2"/></svg>Legal Services</li>
    <li><svg width="11" height="11" viewBox="0 0 11 11"><circle cx="5.5" cy="5.5" r="5" fill="none" stroke="#38b6f5"/><path d="M3 5.6l1.7 1.7L8 4" fill="none" stroke="#38b6f5" stroke-width="1.2"/></svg>Legal Services</li>
    <li><svg width="11" height="11" viewBox="0 0 11 11"><circle cx="5.5" cy="5.5" r="5" fill="none" stroke="#38b6f5"/><path d="M3 5.6l1.7 1.7L8 4" fill="none" stroke="#38b6f5" stroke-width="1.2"/></svg>Valid 30 Day</li>
  </ul>
  <a class="btn-start">Start Now!</a>
</div>
<div class="package-card abs" style="left:298px">
  <div class="package-head">Packages: 4.99</div>
  <ul class="feature-list">
    <li><svg width="11" height="11" viewBox="0 0 11 11"><circle cx="5.5" cy="5.5" r="5" fill="none" stroke="#38b6f5"/><path d="M3 5.6l1.7 1.7L8 4" fill="none" stroke="#38b6f5" stroke-width="1.2"/></svg>Legal Services</li>
    <li><svg width="11" height="11" viewBox="0 0 11 11"><circle cx="5.5" cy="5.5" r="5" fill="none" stroke="#38b6f5"/><path d="M3 5.6l1.7 1.7L8 4" fill="none" stroke="#38b6f5" stroke-width="1.2"/></svg>Legal Services</li>
    <li><svg width="11" height="11" viewBox="0 0 11 11"><circle cx="5.5" cy="5.5" r="5" fill="none" stroke="#38b6f5"/><path d="M3 5.6l1.7 1.7L8 4" fill="none" stroke="#38b6f5" stroke-width="1.2"/></svg>Valid 30 Day</li>
  </ul>
  <a class="btn-start">Start Now!</a>
</div>
<div class="package-card abs" style="left:498px">
  <div class="package-head">Packages: 9.99</div>
  <ul class="feature-list">
    <li><svg width="11" height="11" viewBox="0 0 11 11"><circle cx="5.5" cy="5.5" r="5" fill="none" stroke="#38b6f5"/><path d="M3 5.6l1.7 1.7L8 4" fill="none" stroke="#38b6f5" stroke-width="1.2"/></svg>Legal Services</li>
    <li><svg width="11" height="11" viewBox="0 0 11 11"><circle cx="5.5" cy="5.5" r="5" fill="none" stroke="#38b6f5"/><path d="M3 5.6l1.7 1.7L8 4" fill="none" stroke="#38b6f5" stroke-width="1.2"/></svg>Legal Services</li>
    <li><svg width="11" height="11" viewBox="0 0 11 11"><circle cx="5.5" cy="5.5" r="5" fill="none" stroke="#38b6f5"/><path d="M3 5.6l1.7 1.7L8 4" fill="none" stroke="#38b6f5" stroke-width="1.2"/></svg>Valid 30 Day</li>
  </ul>
  <a class="btn-start">Start Now!</a>
</div>

<div class="gallery-tile abs" style="left:95px;background:#a9a9a9" role="img" aria-label="Slide explaining what Quorvia is and its value proposition"></div>
<div class="gallery-tile abs" style="left:291px;background:linear-gradient(160deg,#2c3350,#1e2436)" role="img" aria-label="Photo slide with statistics on individual proprietorships"></div>
<div class="gallery-tile abs" style="left:487px;background:#a9a9a9" role="img" aria-label="Slide listing what Quorvia provides: legal structure, key documents, connections"></div>

<footer class="site-footer abs"></footer>
<div class="footer-nav abs">Home<span>|</span>Our Team<span>|</span>Contact Us</div>
<div class="footer-brand abs">
  <span class="brand-dot"></span>
  <div><div class="brand-name">Quorvia</div><div class="brand-tag">Legal Made Simple</div></div>
</div>
<div class="social abs" aria-label="Follow us @quorvia.app"><span></span><span></span><span></span><span></span></div>

</body>
</html>
```